Quillmark painting

Am looking for a lawn sign design for my paintings company.
I also attached my business card a example

Phone number of the business +1(204)555-0187
Key words:Free estimates|pressure washing |Residential| Commercial | Interior | Exterior

```html
<!DOCTYPE html>
<html lang="en">
<head>
<meta charset="utf-8">
<title>Quillmark Painting – Lawn Sign</title>
<link href="https://fonts.googleapis.com/css2?family=Poppins:wght@400;500&family=Open+Sans:ital,wght@1,400&family=Roboto+Condensed:wght@700&display=swap" rel="stylesheet">
<style>
  :root {
    --sun: #f6c35a;
    --foliage: #5a6a2a;
    --grass-light: #8fd43a;
    --grass: #3f9a22;
    --grass-deep: #1f5a14;
    --band: rgba(3, 28, 10, 0.88);
    --brand-blue: #00a6e0;
    --white: #ffffff;
    --ink: #000000;
  }
  html, body {
    margin: 0;
    padding: 0;
    width: 1200px;
    height: 900px;
    overflow: hidden;
  }
  .sign {
    position: relative;
    width: 1200px;
    height: 900px;
    overflow: hidden;
    font-family: "Poppins", sans-serif;
  }
  .sign__backdrop {
    position: absolute;
    inset: 0;
    background:
      radial-gradient(ellipse 320px 90px at 560px 60px, rgba(255, 236, 170, 0.95), rgba(255, 236, 170, 0) 100%),
      linear-gradient(180deg, #d99a3c 0px, var(--sun) 40px, var(--foliage) 96px, #1e3d14 300px, var(--grass-deep) 500px, var(--grass) 580px, var(--grass-light) 700px, var(--grass) 900px);
  }
  .sign__band {
    position: absolute;
    left: 0;
    top: 96px;
    width: 1200px;
    height: 423px;
    background: var(--band);
  }
  .brand {
    position: absolute;
    left: 0;
    width: 1200px;
    margin: 0;
    text-align: center;
    color: var(--brand-blue);
    font-weight: 500;
    line-height: 1;
  }
  .brand--name {
    top: 128px;
    font-size: 90px;
    letter-spacing: 4px;
  }
  .brand--trade {
    top: 228px;
    font-size: 72px;
    letter-spacing: 26px;
    padding-left: 26px;
    box-sizing: border-box;
  }
  .services {
    position: absolute;
    left: 0;
    width: 1200px;
    margin: 0;
    text-align: center;
    color: var(--white);
    font-weight: 400;
    font-size: 43px;
    line-height: 1;
  }
  .services--first { top: 341px; }
  .services--second { top: 390px; }
  .contact {
    position: absolute;
    left: 391px;
    top: 482px;
    width: 418px;
    height: 103px;
    background: var(--white);
    text-align: center;
    color: var(--ink);
  }
  .contact__prompt {
    position: absolute;
    top: 13px;
    left: 0;
    width: 100%;
    margin: 0;
    font-family: "Open Sans", sans-serif;
    font-style: italic;
    font-size: 18px;
    line-height: 1;
  }
  .contact__phone {
    position: absolute;
    top: 40px;
    left: 0;
    width: 100%;
    margin: 0;
    font-family: "Roboto Condensed", sans-serif;
    font-weight: 700;
    font-size: 57px;
    line-height: 1;
    letter-spacing: -0.5px;
  }
</style>
</head>
<body>
  <main class="sign">
    <div class="sign__backdrop" role="img" aria-label="Photo of sunlight through trees above a close-up of a fresh green lawn"></div>
    <div class="sign__band"></div>

    <h1 class="brand brand--name">QUILLMARK</h1>
    <p class="brand brand--trade">PAINTING</p>

    <p class="services services--first">FREE ESTIMATES | PRESSURE WASHING</p>
    <p class="services services--second">RESIDENTIAL | COMMERCIAL | INTERIOR | EXTERIOR</p>

    <div class="contact">
      <p class="contact__prompt">Call to find out more</p>
      <p class="contact__phone">+1(204)555-0187</p>
    </div>
  </main>
</body>
</html>
```